New Flyer Design Project*

The business provides eyelash extensions and hair services. Mostly eyelash extension photos and reviews are seen, so please visit www.mirelbeauty.com for more information!

My target audience consists of women aged 18-50 (quite broad) but all demographics is fine. The store is in Lakeway, TX, so while the majority is Caucasian, a lot of diverse customers come in as well!

In terms of ideas, I want a modern approach that is pretty minimal but also depicts examples of eyelash extensions for people to get a visual aid. I like black, gray, white, gold, brown, and green, so a good balance of those would be really nice. I also like to make it really easy to read so that people of older age wouldn't struggle reading it! I would also like a title page, menu, brief history of my services, and referral/contact info on the back.

Colors

Designer to choose colors to be used in the design.

Requirements
Must have
• https://www.ratespot.com/biz/mirel-bella-lakeway

```html
<!DOCTYPE html>
<html lang="en">
<head>
<meta charset="utf-8">
<title>Mirel Bella – Lashes &amp; Beauty Trifold</title>
<link href="https://fonts.googleapis.com/css2?family=Cormorant+Garamond:ital,wght@0,500;0,600;1,600;1,700&family=Lato:ital,wght@0,400;0,700;1,400&display=swap" rel="stylesheet">
<style>
:root{
  --canvas:#e4e4e4;
  --charcoal:#3b3939;
  --gold:#c49a5c;
  --paper:#ffffff;
  --ink:#3a3a3a;
  --muted:#6d6d6d;
  --muted-light:#d6d3d1;
}
*{box-sizing:border-box;margin:0;padding:0}
html,body{width:1200px;height:2402px;overflow:hidden;background:var(--canvas)}
body{position:relative;font-family:'Lato',Arial,sans-serif;color:var(--ink)}
.spread{position:absolute;left:50px;width:1100px;height:850px;display:flex;box-shadow:0 14px 40px rgba(0,0,0,.18)}
.spread--outside{top:250px}
.spread--inside{top:1300px}
.panel{position:relative;width:366.67px;height:850px;overflow:hidden;background:var(--paper)}
.panel + .panel{border-left:1px solid rgba(0,0,0,.06)}
.panel-art{position:absolute;inset:0;width:100%;height:100%}

/* cover */
.brand{position:absolute;top:34px;left:0;right:0;text-align:center}
.brand-mark{width:26px;height:26px;border:2px solid var(--gold);border-radius:50%;margin:0 auto 8px}
.brand-name{font-family:'Cormorant Garamond',Georgia,serif;font-weight:600;font-size:30px;letter-spacing:3px;color:var(--gold)}
.brand-sub{font-family:'Cormorant Garamond',Georgia,serif;font-weight:600;font-size:15px;color:var(--gold);letter-spacing:1px;margin-top:2px}
.cover-copy{position:absolute;left:0;right:0;top:660px;text-align:center}
.cover-title{font-family:'Cormorant Garamond',Georgia,serif;font-weight:600;font-size:38px;color:var(--gold)}
.cover-tagline{font-family:'Cormorant Garamond',Georgia,serif;font-style:italic;font-weight:700;font-size:17px;color:var(--paper);margin-top:8px}
.url-pill{display:inline-block;margin-top:18px;padding:6px 26px;border:1.5px solid var(--gold);border-radius:20px;color:var(--paper);font-size:15px;letter-spacing:1px}

/* about */
.about{position:absolute;top:46px;left:34px;right:30px}
.heading{font-family:'Cormorant Garamond',Georgia,serif;font-weight:600;color:var(--gold);font-size:32px}
.subheading{font-family:'Cormorant Garamond',Georgia,serif;font-style:italic;font-weight:600;color:var(--muted);font-size:15px;margin:2px 0 16px}
.body-text{font-size:12.5px;line-height:1.7;color:var(--muted);font-style:italic}
.body-text + .body-text{margin-top:14px}

/* testimonial */
.quote{position:absolute;top:240px;left:36px;right:36px;text-align:center}
.quote-mark{font-family:'Cormorant Garamond',Georgia,serif;font-size:54px;line-height:.6;color:var(--gold)}
.quote .body-text{margin-top:16px}
.contact{position:absolute;top:620px;left:0;right:0;text-align:center;color:var(--paper);font-size:14px;line-height:1.6;font-style:normal}
.contact-line{display:flex;align-items:center;justify-content:center;gap:8px;margin-top:6px}
.contact-handles{display:flex;justify-content:center;gap:22px;margin-top:6px}
.handle{display:flex;align-items:center;gap:6px}
.handle-box{width:12px;height:12px;background:var(--gold)}

/* menus */
.menu{position:absolute;left:30px;right:30px}
.menu .heading{font-size:27px}
.menu-group{font-family:'Cormorant Garamond',Georgia,serif;font-style:italic;font-weight:700;color:var(--gold);font-size:15px;margin:14px 0 4px;display:flex;justify-content:space-between;align-items:flex-end}
.tiers{font-family:'Lato',Arial,sans-serif;font-style:normal;font-weight:400;font-size:10px;color:var(--muted);display:flex;gap:22px}
.menu-item{display:flex;align-items:flex-end;font-size:14px;line-height:1.3;margin-top:7px}
.item-name{flex:0 0 auto}
.leader{flex:1 1 auto;border-bottom:1.5px dotted currentColor;margin:0 6px 4px;opacity:.7}
.price{flex:0 0 auto;display:flex;gap:12px;font-weight:700}
.on-dark{color:var(--paper)}
.on-dark .body-text{color:var(--muted-light)}
.menu .body-text{margin-top:16px;font-size:12px}
.heading--center{text-align:center}
.section-gap{margin-top:30px}
.note{margin-top:10px}
</style>
</head>
<body>

<!-- OUTSIDE OF TRIFOLD -->
<section class="spread spread--outside">

  <article class="panel panel--about">
    <svg class="panel-art" viewBox="0 0 367 850" preserveAspectRatio="none">
      <path role="img" aria-label="Photo collage of lash clients relaxing during treatment" d="M0 560 C120 520 250 540 367 500 V850 H0Z" fill="#b89c86"/>
      <path d="M0 560 C120 520 250 540 367 500" fill="none" stroke="#c49a5c" stroke-width="4"/>
      <circle role="img" aria-label="Close-up photo of a client with lash extensions" cx="110" cy="610" r="52" fill="#d8c2b0" stroke="#c49a5c" stroke-width="4"/>
      <circle role="img" aria-label="Close-up photo of an eye with lashes" cx="210" cy="640" r="36" fill="#8f7464" stroke="#c49a5c" stroke-width="3"/>
    </svg>
    <div class="about">
      <h2 class="heading">About Us</h2>
      <p class="subheading">What is Mirel Bella?</p>
      <p class="body-text">To always deliver more than expected, we at Mirel Bella take care to treat every guest like family. Our friendly, highly trained artists use premium products and gentle techniques so your lashes look natural and feel light.</p>
      <p class="body-text">Mirel Bella is the place to unwind, refresh and leave feeling confident, with lashes that last and service you can trust every visit.</p>
    </div>
  </article>

  <article class="panel panel--contact">
    <svg class="panel-art" viewBox="0 0 367 850" preserveAspectRatio="none">
      <path d="M0 590 C120 540 250 560 367 520 V850 H0Z" fill="var(--charcoal)"/>
      <path d="M0 582 C120 532 250 552 367 512" fill="none" stroke="#c49a5c" stroke-width="4"/>
      <circle cx="183" cy="125" r="84" fill="none" stroke="#c49a5c" stroke-width="4"/>
      <circle role="img" aria-label="Close-up photo of an eye wearing lash extensions" cx="183" cy="125" r="76" fill="#c9ad95"/>
    </svg>
    <div class="quote">
      <div class="quote-mark">&ldquo;</div>
      <p class="body-text">My eyes look bigger and brighter every single day. The artists here are careful, kind and truly talented, and my lashes always last for weeks. I would not go anywhere else, and I tell all my friends about this place!</p>
    </div>
    <address class="contact">
      <div>418 Cedar Crest Road</div>
      <div>Willow Bend, TX 78641</div>
      <div class="contact-line">
        <svg width="14" height="14" viewBox="0 0 24 24" aria-hidden="true"><path d="M6.6 10.8a15 15 0 0 0 6.6 6.6l2.2-2.2a1 1 0 0 1 1-.25 11.4 11.4 0 0 0 3.6.6 1 1 0 0 1 1 1V20a1 1 0 0 1-1 1A17 17 0 0 1 3 4a1 1 0 0 1 1-1h3.5a1 1 0 0 1 1 1c0 1.25.2 2.45.6 3.6a1 1 0 0 1-.25 1z" fill="#c49a5c"/></svg>
        (512) 555-0147
      </div>
      <div class="contact-handles">
        <span class="handle"><span class="handle-box"></span>@mirelbella</span>
        <span class="handle"><span class="handle-box"></span>@mirelbella</span>
      </div>
      <span class="url-pill">www.mirelbeauty.com</span>
    </address>
  </article>

  <article class="panel panel--cover">
    <svg class="panel-art" viewBox="0 0 367 850" preserveAspectRatio="none">
      <defs>
        <linearGradient id="coverPhoto" x1="0" y1="0" x2="1" y2="1">
          <stop offset="0" stop-color="#e9ddd0"/>
          <stop offset=".55" stop-color="#7a5440"/>
          <stop offset="1" stop-color="#4a3024"/>
        </linearGradient>
      </defs>
      <path role="img" aria-label="Portrait photo of a woman with long wavy brown hair and lash extensions" d="M0 140 H367 V300 C330 520 160 630 0 580 Z" fill="url(#coverPhoto)"/>
      <path d="M0 580 C160 630 330 520 367 300 V850 H0Z" fill="var(--charcoal)"/>
      <path d="M0 592 C165 642 340 528 367 320" fill="none" stroke="#c49a5c" stroke-width="5"/>
    </svg>
    <header class="brand">
      <div class="brand-mark"></div>
      <div class="brand-name">MIREL BELLA</div>
      <div class="brand-sub">Lashes ~ Beauty</div>
    </header>
    <div class="cover-copy">
      <h1 class="cover-title">Lashes &amp; Beauty</h1>
      <p class="cover-tagline">Get Ready To Bat Those Eyelashes With Confidence!</p>
      <span class="url-pill">www.mirelbeauty.com</span>
    </div>
  </article>
</section>

<!-- INSIDE OF TRIFOLD -->
<section class="spread spread--inside">

  <article class="panel panel--classic">
    <svg class="panel-art" viewBox="0 0 367 850" preserveAspectRatio="none">
      <rect width="367" height="850" fill="var(--charcoal)"/>
      <path role="img" aria-label="Photo of a lash artist applying extensions with tweezers" d="M0 640 C120 600 250 610 367 580 V850 H0Z" fill="#c7a48c"/>
      <path d="M0 632 C120 592 250 602 367 572" fill="none" stroke="#c49a5c" stroke-width="4"/>
    </svg>
    <div class="menu on-dark" style="top:40px">
      <h2 class="heading">Velvet Classic Lash</h2>
      <div class="menu-group">Lash Extensions Full Set<span class="tiers"><span>Artist</span><span>Master</span></span></div>
      <div class="menu-item"><span class="item-name">Classic Extension<br>Natural lashes</span><span class="leader"></span><span class="price"><span>$145</span><span>$165</span></span></div>
      <div class="menu-item"><span class="item-name">Classic Extension<br>Full lashes</span><span class="leader"></span><span class="price"><span>$155</span><span>$185</span></span></div>
      <div class="menu-group">Lash Extensions Refill<span class="tiers"><span>Artist</span><span>Master</span></span></div>
      <div class="menu-item"><span class="item-name">Velvet Classic<br>2-3 Weeks</span><span class="leader"></span><span class="price"><span>$65</span><span>$75</span></span></div>
      <div class="menu-item"><span class="item-name">Velvet Classic<br>3-4 Weeks</span><span class="leader"></span><span class="price"><span>$75</span><span>$85</span></span></div>
      <p class="body-text">CLASSIC EXTENSIONS apply one single extension to each natural lash. The result is a soft, natural look that adds length and curl. Extensions come in several lengths and thicknesses to suit each eye.</p>
    </div>
  </article>

  <article class="panel panel--volume">
    <svg class="panel-art" viewBox="0 0 367 850" preserveAspectRatio="none">
      <path role="img" aria-label="Photo of a bride having her makeup and lashes done" d="M0 480 C120 450 250 470 367 440 V600 C250 630 120 610 0 640Z" fill="#d4b9a3"/>
      <path d="M0 640 C120 610 250 630 367 600" fill="none" stroke="#c49a5c" stroke-width="4"/>
    </svg>
    <div class="menu" style="top:36px">
      <h2 class="heading">Aurora Volume Lashes</h2>
      <div class="menu-group">Lash Extensions Full Set<span class="tiers"><span>Artist</span><span>Master</span></span></div>
      <div class="menu-item"><span class="item-name">Volume Extension<br>Lux</span><span class="leader"></span><span class="price"><span>$195</span><span>$205</span></span></div>
      <div class="menu-item"><span class="item-name">Volume Extension<br>Max</span><span class="leader"></span><span class="price"><span>$205</span><span>$215</span></span></div>
      <div class="menu-group">Lash Extensions Refill</div>
      <div class="menu-item"><span class="item-name">Volume Extension<br>2-3 Weeks</span><span class="leader"></span><span class="price"><span>$75</span><span>$85</span></span></div>
      <div class="menu-item"><span class="item-name">Volume Extension<br>3-4 Weeks</span><span class="leader"></span><span class="price"><span>$85</span><span>$95</span></span></div>
      <p class="body-text note">VOLUME EXTENSIONS place a fan of two to six fine lashes on each natural lash for a fuller, fluffier look that still feels light and comfortable.</p>
    </div>
    <div class="menu" style="top:660px">
      <h2 class="heading heading--center">Radiance Lash Set</h2>
      <div class="menu-item"><span class="item-name">Special Volume Extension</span><span class="leader"></span><span class="price"><span>$235</span></span></div>
      <div class="menu-item"><span class="item-name">Re-fill 3-4 Weeks</span><span class="leader"></span><span class="price"><span>$115</span></span></div>
      <p class="body-text note">Perfect for a special occasion, wedding or photo shoot. Imagine waking up looking glamorous without doing anything.</p>
    </div>
  </article>

  <article class="panel panel--hair">
    <svg class="panel-art" viewBox="0 0 367 850" preserveAspectRatio="none">
      <rect width="367" height="850" fill="var(--charcoal)"/>
      <path role="img" aria-label="Photo of a stylist straightening a client's hair in the salon" d="M0 0 H367 V240 C250 290 120 320 0 360Z" fill="#a88470"/>
      <path d="M0 368 C120 328 250 298 367 248" fill="none" stroke="#c49a5c" stroke-width="4"/>
    </svg>
    <div class="menu on-dark" style="top:420px">
      <h2 class="heading">Lash Extension Removal</h2>
      <div class="menu-item"><span class="item-name">Extension Removal - Current Client</span><span class="leader"></span><span class="price"><span>$0</span></span></div>
      <div class="menu-item"><span class="item-name">Extension Removal - New Client</span><span class="leader"></span><span class="price"><span>$30</span></span></div>
      <h2 class="heading section-gap">Hair Service</h2>
      <div class="menu-item"><span class="item-name">Women hair cut</span><span class="leader"></span><span class="price"><span>$45 and up</span></span></div>
      <div class="menu-item"><span class="item-name">Men hair cut</span><span class="leader"></span><span class="price"><span>$30</span></span></div>
      <div class="menu-item"><span class="item-name">Children hair cut</span><span class="leader"></span><span class="price"><span>$25</span></span></div>
      <div class="menu-item"><span class="item-name">Shampoo hair style</span><span class="leader"></span><span class="price"><span>$35</span></span></div>
      <div class="menu-item"><span class="item-name">Updo</span><span class="leader"></span><span class="price"><span>$65 and up</span></span></div>
    </div>
  </article>
</section>

</body>
</html>
```